Akademie für Wahrnehmungspflege
Zielgruppe
Ich biete die beiden Seminare 'Kraftquell im Jahreslauf' und 'Feinsinn im Wochenlauf' an. Die Zielgruppe sind spirituell interessierte Leute.
Aufgabenstellung
Die Anzeige sollte mehr oder weniger mit den Farben meiner Webseite übereinstimmen (www.am-ruhepol.ch).
Grösse der Anzeige:
breit: 121mm
hoch: 124mm
Die Anzeige sollte mein persönliches Bild und das Logo enthalten.
Text:
Feinsinn im Wochenlauf:
Seminare zur Förderung Ihrer Intuition. Entdecken Sie Ihre eigene Medialität und lernen Sie diese gezielt im Alltag einzusetzen.
26./27. August 2017
11./12. November 2017
Kraftquell im Jahreslauf:
Seminare für energetisches Heilen. Lernen Sie sich und andere Menschen energetisch zu begleiten.
16./17. September 2017
9./10. Dezember 2017
2 für 1 - Aktion:
Kommen Sie zu zweit und bezahlen Sie nur für eine Person
(gültig bis Ende 2017)
Webseite:
www.am-ruhepol.ch
Seminarort: Grünmattenhof, 3470 Lindenmoos, Schweiz

```html
<!DOCTYPE html>
<html lang="de">
<head>
<meta charset="utf-8">
<title>Akademie für Wahrnehmungspflege – Seminare</title>
<link href="https://fonts.googleapis.com/css2?family=Barlow:wght@400;500;600;700&family=Barlow+Semi+Condensed:wght@600;700&display=swap" rel="stylesheet">
<style>
  :root {
    --blue: #4f88c6;
    --blue-light: #b9d0ee;
    --orange: #f28a00;
    --white: #ffffff;
    --logo-blue: #3d7cc2;
  }
  * { box-sizing: border-box; margin: 0; padding: 0; }
  html, body { width: 1172px; height: 1200px; overflow: hidden; background: var(--white); }
  .ad {
    position: relative;
    width: 1172px;
    height: 1200px;
    background: var(--white);
    font-family: "Barlow", Arial, sans-serif;
    color: var(--white);
    overflow: hidden;
  }
  .ad__panel {
    position: absolute;
    left: 0; top: 234px;
    width: 1172px; height: 966px;
    background: var(--blue);
  }
  .brand {
    position: absolute;
    left: 610px; top: 70px;
    display: flex; align-items: center; gap: 18px;
  }
  .brand__mark {
    width: 46px; height: 46px; border-radius: 50%;
    background: var(--logo-blue);
  }
  .brand__name {
    font-weight: 500;
    font-size: 30px;
    line-height: 1.15;
    color: var(--logo-blue);
    width: 380px;
  }
  .web-band {
    position: absolute;
    left: 440px; top: 234px;
    width: 732px; height: 56px;
    background: var(--orange);
    padding-left: 32px;
    font-size: 33px;
    font-weight: 500;
    line-height: 56px;
    letter-spacing: 0.5px;
  }
  .portrait {
    position: absolute;
    left: 77px; top: 49px;
    width: 360px; height: 357px;
    border: 8px solid var(--white);
    background: linear-gradient(135deg, #d9d9d9 0%, #8f8f8f 55%, #4a4a4a 100%);
    box-shadow: 0 0 2px rgba(0,0,0,0.25);
  }
  .person-name {
    position: absolute;
    left: 472px; top: 308px;
    font-size: 25px;
    font-weight: 400;
    letter-spacing: 0.5px;
  }
  .seminar { position: absolute; left: 77px; }
  .seminar--feinsinn { top: 455px; }
  .seminar--kraftquell { top: 750px; }
  .seminar__title {
    font-family: "Barlow Semi Condensed", Arial, sans-serif;
    font-weight: 700;
    font-size: 41px;
    letter-spacing: 1px;
    color: var(--blue-light);
    text-transform: uppercase;
    line-height: 1;
    margin-bottom: 16px;
  }
  .seminar__text {
    font-size: 25.5px;
    font-weight: 500;
    line-height: 40px;
    letter-spacing: 0.3px;
  }
  .seminar__dates { list-style: none; margin-top: 16px; }
  .seminar--kraftquell .seminar__dates { margin-top: 22px; }
  .seminar__dates li {
    font-size: 27px;
    font-weight: 500;
    line-height: 38px;
    display: flex; align-items: center; gap: 12px;
  }
  .seminar__dates svg { width: 22px; height: 20px; flex: none; }
  .divider {
    position: absolute;
    left: 49px; width: 1074px; height: 0;
    border-top: 3px dotted rgba(255,255,255,0.75);
  }
  .divider--first { top: 717px; }
  .divider--second { top: 1089px; }
  .offer {
    position: absolute;
    left: 764px; top: 572px;
    width: 362px; height: 362px;
    border-radius: 50%;
    background: var(--orange);
    transform: rotate(-8deg);
    display: flex; flex-direction: column; align-items: center; justify-content: center;
    text-align: center;
  }
  .offer__title {
    font-family: "Barlow Semi Condensed", Arial, sans-serif;
    font-weight: 700;
    font-size: 56px;
    line-height: 1.02;
    text-transform: uppercase;
    margin-top: -12px;
    margin-bottom: 12px;
  }
  .offer__text { font-size: 25px; font-weight: 600; line-height: 1.2; }
  .offer__note { font-size: 16px; font-weight: 500; margin-top: 6px; }
  .venue {
    position: absolute;
    right: 44px; top: 1136px;
    font-size: 26px;
    font-weight: 500;
    letter-spacing: 0.3px;
  }
</style>
</head>
<body>
<main class="ad">
  <div class="ad__panel"></div>

  <div class="brand">
    <span class="brand__mark"></span>
    <span class="brand__name">Akademie für Wahrnehmungspflege</span>
  </div>

  <div class="portrait" role="img" aria-label="Schwarzweiss-Porträtfoto von Lukas Verneuil"></div>

  <div class="web-band">www.am-ruhepol.ch</div>
  <div class="person-name">Lukas Verneuil</div>

  <section class="seminar seminar--feinsinn">
    <h2 class="seminar__title">Feinsinn im Wochenlauf:</h2>
    <p class="seminar__text">Seminare zur Förderung Ihrer Intuition. Entdecken Sie Ihre eigene<br>Medialität und lernen Sie diese gezielt im Alltag einzusetzen.</p>
    <ul class="seminar__dates">
      <li><svg viewBox="0 0 22 20"><path d="M0 0 L22 10 L0 20 L6 10 Z" fill="#fff"/></svg>26./27. August 2017</li>
      <li><svg viewBox="0 0 22 20"><path d="M0 0 L22 10 L0 20 L6 10 Z" fill="#fff"/></svg>11./12. November 2017</li>
    </ul>
  </section>

  <div class="divider divider--first"></div>

  <section class="seminar seminar--kraftquell">
    <h2 class="seminar__title">Kraftquell im Jahreslauf:</h2>
    <p class="seminar__text">Seminare für energetisches Heilen.<br>Lernen Sie sich und andere Menschen<br>energetisch zu begleiten.</p>
    <ul class="seminar__dates">
      <li><svg viewBox="0 0 22 20"><path d="M0 0 L22 10 L0 20 L6 10 Z" fill="#fff"/></svg>16./17. September 2017</li>
      <li><svg viewBox="0 0 22 20"><path d="M0 0 L22 10 L0 20 L6 10 Z" fill="#fff"/></svg>9./10. Dezember 2017</li>
    </ul>
  </section>

  <div class="divider divider--second"></div>

  <aside class="offer">
    <p class="offer__title">2 für 1<br>Aktion:</p>
    <p class="offer__text">Kommen Sie zu zweit<br>und bezahlen Sie nur<br>für eine Person</p>
    <p class="offer__note">(gültig bis Ende 2017)</p>
  </aside>

  <p class="venue">Seminarort: Grünmattenhof, 3470 Lindenmoos, Schweiz</p>
</main>
</body>
</html>
```